Business Card Design

We Import cars and commercial vehicles, we have been in business around 12 years, we are based in Christchurch, New Zealand.
I really like the web address on card, possibly right along the bottom of the card?
We specialize in commercial vans, maybe worth a mention?
The logo has the name in it so probably don't need to have twice?

I really like a clean smart look, not too cluttered

Industry/Entity Type

Business

Contact Information for Business Card

DLQ NIPPON MOTORS, Garth Whitmore, Managing Director
web address: www.dlqnippon.example
cell phone. 021 584 217

Requirements
Must have
• the logo, and all the contact details.

Forgot to add my email address, garth@dlqnippon.example
Nice to have
• Just thinking as the card is looking a little empty maybe somewhere written what we do? 'Specializing in commercial vans'
Not sure but we import Japanese vehicles, possibly adding some brands like Velkora Parvex Quillo Rundel etc? Not sure on that one.

```html
<!DOCTYPE html>
<html lang="en">
<head>
<meta charset="utf-8">
<title>DLQ Nippon Motors – Business Card</title>
<link rel="stylesheet" href="https://fonts.googleapis.com/css2?family=Open+Sans:wght@300;400;700;800&display=swap">
<style>
  :root {
    --card-top: #050505;
    --card-mid: #1c1c1c;
    --card-bottom: #3b3b3b;
    --orange: #f7941d;
    --white: #ffffff;
    --soft-grey: #cfcfcf;
    --icon-grey: #c4c4c4;
    --rule-grey: #8a8a8a;
  }
  * { margin: 0; padding: 0; box-sizing: border-box; }
  html, body {
    width: 1200px;
    height: 741px;
    overflow: hidden;
    background: var(--card-top);
  }
  .card {
    position: relative;
    width: 1200px;
    height: 741px;
    overflow: hidden;
    font-family: "Open Sans", Arial, sans-serif;
    background: linear-gradient(180deg, var(--card-top) 0%, var(--card-mid) 40%, var(--card-bottom) 100%);
  }
  .backdrop-vehicle {
    position: absolute;
    left: 120px;
    top: 140px;
    width: 1080px;
    height: 601px;
    background: radial-gradient(ellipse at 65% 55%, rgba(255,255,255,0.07) 0%, rgba(255,255,255,0.03) 45%, rgba(255,255,255,0) 75%);
  }
  .brand {
    position: absolute;
    left: 58px;
    top: 58px;
    color: var(--white);
    font-weight: 800;
    font-size: 52px;
    line-height: 56px;
    letter-spacing: 0.01em;
  }
  .brand-rule {
    position: absolute;
    left: 0;
    top: 186px;
    width: 920px;
    height: 9px;
    background: linear-gradient(90deg, var(--rule-grey) 0%, #6a6a6a 60%, rgba(80,80,80,0) 100%);
  }
  .person-name {
    position: absolute;
    left: 162px;
    top: 224px;
    font-size: 41px;
    line-height: 48px;
    letter-spacing: 0.12em;
    color: var(--orange);
    text-transform: uppercase;
  }
  .person-name .given { font-weight: 700; }
  .person-name .family { font-weight: 300; }
  .person-role {
    position: absolute;
    left: 162px;
    top: 272px;
    font-size: 36px;
    line-height: 44px;
    font-weight: 300;
    color: var(--soft-grey);
  }
  .contact-line {
    position: absolute;
    left: 178px;
    display: flex;
    align-items: center;
    font-size: 38px;
    font-weight: 300;
    color: var(--soft-grey);
  }
  .contact-line .icon {
    width: 54px;
    display: flex;
    justify-content: center;
    margin-right: 33px;
  }
  .contact-phone { top: 354px; }
  .contact-email { top: 428px; }
  .web-footer {
    position: absolute;
    left: 162px;
    top: 616px;
    display: flex;
    align-items: center;
    font-size: 35px;
    line-height: 48px;
    letter-spacing: 0.32em;
    text-transform: uppercase;
  }
  .web-footer .label { color: var(--white); font-weight: 300; }
  .web-footer .divider {
    width: 2px;
    height: 44px;
    background: var(--white);
    margin: 0 30px 0 8px;
  }
  .web-footer .address { color: var(--orange); font-weight: 700; }
</style>
</head>
<body>
  <div class="card">
    <div class="backdrop-vehicle" role="img" aria-label="Faint outline drawing of a commercial van front in the background"></div>

    <div class="brand">DLQ NIPPON<br>MOTORS</div>
    <div class="brand-rule"></div>

    <h1 class="person-name"><span class="given">Garth</span><span class="family">Whitmore</span></h1>
    <p class="person-role">Managing Director</p>

    <div class="contact-line contact-phone">
      <span class="icon">
        <svg width="30" height="54" viewBox="0 0 30 54" aria-hidden="true">
          <rect x="1.5" y="1.5" width="27" height="51" rx="4" fill="none" stroke="var(--icon-grey)" stroke-width="3"/>
          <line x1="1.5" y1="9" x2="28.5" y2="9" stroke="var(--icon-grey)" stroke-width="2"/>
          <line x1="1.5" y1="42" x2="28.5" y2="42" stroke="var(--icon-grey)" stroke-width="2"/>
          <circle cx="15" cy="47.5" r="2" fill="var(--icon-grey)"/>
        </svg>
      </span>
      <span class="value">021 584 217</span>
    </div>

    <div class="contact-line contact-email">
      <span class="icon">
        <svg width="52" height="34" viewBox="0 0 52 34" aria-hidden="true">
          <rect x="0" y="0" width="52" height="34" fill="var(--icon-grey)"/>
          <polyline points="1,1 26,20 51,1" fill="none" stroke="#2a2a2a" stroke-width="2"/>
        </svg>
      </span>
      <span class="value">garth@dlqnippon.example</span>
    </div>

    <div class="web-footer">
      <span class="label">Visit</span>
      <span class="divider"></span>
      <span class="address">www.dlqnippon.example</span>
    </div>
  </div>
</body>
</html>
```